Australian Civil Construction, Quarry & Mining Services needs a business card

We need a business card designed for our Civil Construction, Quarry & Mining Services based in the country in Australia.
Our Company Brackley Earthworks provide innovate solutions for infrastructure, agricultural and mining (aggregate, sand, roadbase) industry.
We would like our business cards to be double sided
Front of card: black background or something that resembles our business colours. (it doesn't have to be black we are open to options)
- Company name - Brackley Earthworks
- Either our logo or some sort of icon/picture that resembles our business
- Website - https://brackleyearthworks.com.au/
- We will have a number of different names, positions descriptions, phone numbers and emails on separate cards for each of our managers/directors

```html
<!DOCTYPE html>
<html lang="en">
<head>
<meta charset="utf-8">
<title>Brackley Earthworks – Business Card</title>
<link href="https://fonts.googleapis.com/css2?family=Barlow+Condensed:ital,wght@0,300;0,500;0,700;0,800;1,600&display=swap" rel="stylesheet">
<style>
  :root {
    --canvas: #c8c8c7;
    --ink: #000000;
    --white: #ffffff;
    --orange: #f7821b;
    --orange-bright: #fc8418;
    --orange-mid: #e2700f;
    --orange-deep: #b0500a;
    --charcoal: #2a2a2a;
  }
  * { margin: 0; padding: 0; box-sizing: border-box; }
  html, body {
    width: 1200px; height: 1200px; overflow: hidden;
    background: var(--canvas);
    font-family: "Barlow Condensed", "Arial Narrow", sans-serif;
  }
  .canvas { position: relative; width: 1200px; height: 1200px; }

  .card { position: absolute; width: 757px; height: 438px; overflow: hidden; }

  /* Front */
  .card--front { left: 234px; top: 125px; }
  .front__stage {
    position: absolute; left: 0; top: 0; width: 100%; height: 354px;
    background:
      radial-gradient(ellipse 340px 240px at 390px 220px, rgba(80,52,28,0.55), rgba(40,26,14,0.25) 55%, rgba(0,0,0,0) 80%),
      radial-gradient(ellipse 420px 300px at 420px 210px, #333 0%, #151515 50%, #000 80%);
  }
  .brand {
    position: absolute; left: 84px; top: 118px;
    display: flex; align-items: center; gap: 26px;
  }
  .brand__mark { width: 112px; height: 112px; background: var(--orange); flex: none; }
  .brand__name {
    color: var(--orange);
    font-weight: 800; font-size: 66px; line-height: 0.9;
    letter-spacing: 1px; text-transform: uppercase;
  }
  .services {
    position: absolute; left: 0; top: 354px; width: 100%; height: 84px;
    background: linear-gradient(180deg, var(--orange-bright) 0%, var(--orange-mid) 55%, var(--orange-deep) 100%);
    display: flex; align-items: center; justify-content: center; gap: 12px;
    color: var(--ink); font-weight: 700; font-size: 35px; letter-spacing: 0.5px;
  }
  .services__sep { width: 10px; height: 9px; }

  /* Back */
  .card--back {
    left: 238px; top: 602px;
    background: radial-gradient(ellipse 520px 380px at 370px 218px, var(--orange-bright) 0%, var(--orange-mid) 50%, var(--orange-deep) 100%);
  }
  .person { position: absolute; left: 378px; top: 72px; }
  .person__name { font-size: 42px; line-height: 1; color: var(--ink); letter-spacing: 0.3px; }
  .person__first { font-weight: 300; }
  .person__last { font-weight: 700; }
  .person__role { margin-top: 6px; font-size: 25px; font-style: italic; font-weight: 600; letter-spacing: 0.3px; }
  .divider { position: absolute; left: 383px; top: 155px; width: 266px; height: 2px; background: var(--ink); }

  .contact { position: absolute; left: 380px; top: 233px; list-style: none; }
  .contact__item {
    display: flex; align-items: center; height: 44px;
    font-size: 29px; font-weight: 500; color: var(--ink);
  }
  .contact__icon { width: 28px; height: 28px; margin-right: 14px; flex: none; }
</style>
</head>
<body>
<main class="canvas">

  <section class="card card--front" aria-label="Business card front">
    <div class="front__stage">
      <div class="brand">
        <span class="brand__mark"></span>
        <h1 class="brand__name">Brackley<br>Earthworks</h1>
      </div>
    </div>
    <div class="services">
      <span>SERVICES1</span>
      <svg class="services__sep" viewBox="0 0 10 9"><path d="M5 0 L10 9 H0 Z" fill="#000"/></svg>
      <span>SERVICE 2</span>
      <svg class="services__sep" viewBox="0 0 10 9"><path d="M5 0 L10 9 H0 Z" fill="#000"/></svg>
      <span>SERVICE 3</span>
    </div>
  </section>

  <section class="card card--back" aria-label="Business card back">
    <div class="person">
      <p class="person__name"><span class="person__first">FIRST</span> <span class="person__last">LASTNAME</span></p>
      <p class="person__role">MANAGER</p>
    </div>
    <div class="divider"></div>
    <ul class="contact">
      <li class="contact__item">
        <svg class="contact__icon" viewBox="0 0 24 24"><path fill="#000" d="M6.6 2.5c.6-.4 1.4-.2 1.8.4l2 3.3c.4.6.2 1.4-.3 1.8L8.6 9.2c.9 2.6 3 5 5.6 6.3l1.3-1.5c.5-.5 1.2-.6 1.8-.2l3.2 2.1c.6.4.8 1.2.4 1.8l-1.4 2.3c-.5.8-1.5 1.2-2.4 1C9.9 19.6 4.5 13.8 3.2 6.6c-.2-.9.2-1.8 1-2.3z"/></svg>
        <span>01 2345 6789</span>
      </li>
      <li class="contact__item">
        <svg class="contact__icon" viewBox="0 0 24 24"><rect x="0.5" y="5" width="23" height="15" fill="#000"/><path d="M2 6.5 L12 13.5 L22 6.5" fill="none" stroke="#e2700f" stroke-width="1.8"/></svg>
        <span>name@emailname.com.au</span>
      </li>
      <li class="contact__item">
        <svg class="contact__icon" viewBox="0 0 24 24"><circle cx="12" cy="12" r="10.5" fill="#000"/><g fill="none" stroke="#e2700f" stroke-width="1.4"><ellipse cx="12" cy="12" rx="4.5" ry="10.5"/><path d="M1.5 12 H22.5 M3.5 6.5 H20.5 M3.5 17.5 H20.5"/></g></svg>
        <span>brackleyearthworks.com.au</span>
      </li>
    </ul>
  </section>

</main>
</body>
</html>
```